DESIGN OF STATIONERY - TALVORA MED

WE WORK IN THE FIELD OF HEALTH (IMAGING: MRI - CT ETC.).
WE WOULD LIKE TO CREATE THE ENTIRE STATIONERY DESIGN : LETTERHEAD, BUSINESS CARD, CALENDAR, INVOICES, CD HOLDER, ETC.

Target Market(s)

PERSONS UNDERTAKING HEALTH EXAMINATIONS

```html
<!DOCTYPE html>
<html lang="en">
<head>
<meta charset="utf-8">
<title>Talvora Med — Stationery</title>
<link rel="stylesheet" href="https://fonts.googleapis.com/css2?family=Montserrat:wght@400;500;700&display=swap">
<style>
  :root{
    --teal:#10a89a;
    --teal-dark:#0c8f83;
    --teal-soft:#5fc9bd;
    --blue:#3b5fb0;
    --blue-soft:#7d95cf;
    --paper:#ffffff;
    --ground:#e6e9ec;
    --ink:#3a4750;
    --ink-light:#8a96a0;
  }
  *{box-sizing:border-box;margin:0;padding:0}
  html,body{width:1014px;height:1200px;overflow:hidden}
  body{background:var(--ground);font-family:"Montserrat",Arial,sans-serif;color:var(--ink);position:relative}
  .piece{position:absolute;background:var(--paper);overflow:hidden;box-shadow:0 2px 8px rgba(30,40,60,.12)}
  .wordmark{font-family:"Montserrat",Arial,sans-serif;font-weight:700;letter-spacing:.02em;color:var(--teal);white-space:nowrap}
  .wordmark.on-colour{color:var(--paper)}
  .tagline{font-size:7px;font-weight:500;color:var(--ink-light);letter-spacing:.05em;margin-top:2px}
  .on-colour + .tagline,.tagline.light{color:rgba(255,255,255,.8)}
  .cross-band{position:absolute;left:0;right:0;bottom:0;
    background:linear-gradient(180deg,rgba(255,255,255,0) 0%,var(--teal-soft) 45%,var(--teal) 70%,var(--blue) 100%)}
  .cross-band.vertical{top:0;bottom:0;left:auto;right:0;
    background:linear-gradient(90deg,rgba(255,255,255,0) 0%,rgba(255,255,255,.55) 45%,rgba(255,255,255,.9) 100%)}
  .cross-band.blue{background:linear-gradient(180deg,rgba(59,95,176,0) 0%,rgba(255,255,255,.45) 60%,rgba(255,255,255,.75) 100%)}

  /* business card front */
  .card-front{left:40px;top:40px;width:360px;height:205px;border-radius:0 0 0 0}
  .card-front .brand{position:absolute;left:40px;top:52px}
  .card-front .wordmark{font-size:26px}
  .card-front .cross-band{height:70px}

  /* business card back */
  .card-back{left:40px;top:275px;width:360px;height:205px;background:var(--teal);color:var(--paper)}
  .card-back .holder{position:absolute;left:40px;top:38px}
  .card-back .holder-name{font-size:18px;font-weight:400;letter-spacing:.03em}
  .card-back .holder-role{font-size:8px;opacity:.85;margin-top:3px}
  .card-back .contacts{position:absolute;left:40px;top:104px;font-size:9px;line-height:1.7}
  .card-back .wordmark{position:absolute;right:22px;top:40px;font-size:11px}
  .card-back .pulse{position:absolute;left:14px;bottom:20px}

  /* cover panel */
  .cover{left:430px;top:40px;width:544px;height:440px;background:var(--teal)}
  .cover .brand{position:absolute;left:70px;top:190px}
  .cover .wordmark{font-size:34px}
  .cover .cross-band{width:200px}

  /* letterhead */
  .letterhead{left:40px;top:520px;width:280px;height:390px}
  .letterhead .brand{position:absolute;left:26px;top:30px}
  .letterhead .wordmark{font-size:18px}
  .letterhead .cross-band{height:80px}
  .letterhead .lines{position:absolute;left:26px;right:26px;top:110px}
  .letterhead .lines span{display:block;height:4px;background:#eef1f3;margin-bottom:12px}

  /* envelope */
  .envelope{left:350px;top:520px;width:330px;height:210px}
  .envelope .flap{position:absolute;left:0;top:0}
  .envelope .brand{position:absolute;left:110px;top:90px}
  .envelope .wordmark{font-size:20px}
  .envelope .cross-band{height:55px}

  /* folder */
  .folder{left:710px;top:520px;width:264px;height:390px;background:var(--blue)}
  .folder .brand{position:absolute;left:30px;top:120px}
  .folder .wordmark{font-size:22px}
  .folder .cross-band{height:110px}

  /* compliments slip */
  .slip{left:350px;top:760px;width:330px;height:150px}
  .slip .accent{position:absolute;left:0;top:0;bottom:0;width:10px;background:var(--teal)}
  .slip .brand{position:absolute;left:36px;top:36px}
  .slip .wordmark{font-size:18px}
  .slip .cross-band{height:45px}

  /* id badge */
  .badge{left:40px;top:950px;width:210px;height:210px;background:var(--blue);color:var(--paper)}
  .badge .photo{position:absolute;left:75px;top:34px;width:60px;height:60px;border-radius:50%;background:linear-gradient(135deg,#c9d3e6,#9fb0d4)}
  .badge .name{position:absolute;left:0;right:0;top:108px;text-align:center;font-size:12px;font-weight:500}
  .badge .role{position:absolute;left:0;right:0;top:126px;text-align:center;font-size:8px;opacity:.85}
  .badge .cross-band{height:50px}

  /* small cards */
  .mini-white{left:280px;top:950px;width:200px;height:110px}
  .mini-white .brand{position:absolute;left:22px;top:26px}
  .mini-white .wordmark{font-size:15px}
  .mini-white .cross-band{height:34px}
  .mini-blue{left:280px;top:1080px;width:200px;height:80px;background:var(--blue)}
  .mini-blue .wordmark{position:absolute;left:22px;top:30px;font-size:13px}

  /* tote */
  .tote{left:510px;top:940px;width:464px;height:220px}
  .tote .strap{position:absolute;left:0;top:0;bottom:0;width:14px;background:var(--teal)}
  .tote .edge{position:absolute;left:30px;top:20px;bottom:20px;width:2px;background:var(--blue)}
  .tote .brand{position:absolute;left:150px;top:70px}
  .tote .wordmark{font-size:28px}
  .tote .cross-band{height:60px;left:14px}
</style>
</head>
<body>

  <section class="piece card-front" aria-label="Business card, front">
    <div class="brand">
      <div class="wordmark">TALVORA MED</div>
      <div class="tagline">Health Care Diagnostic</div>
    </div>
    <div class="cross-band" role="img" aria-label="Scattered medical cross pattern in teal and blue"></div>
  </section>

  <section class="piece card-back" aria-label="Business card, back">
    <div class="holder">
      <div class="holder-name">Dr. Elias Moran</div>
      <div class="holder-role">Chief Radiologist</div>
    </div>
    <div class="wordmark on-colour">TALVORA MED</div>
    <div class="contacts">
      <div>0400-1200-300</div>
      <div>care@talvoramed.com</div>
      <div>www.talvoramed.com</div>
    </div>
    <svg class="pulse" width="330" height="34" viewBox="0 0 330 34" aria-hidden="true">
      <polyline points="0,24 10,24 15,8 21,30 27,14 32,24 330,24" fill="none" stroke="#ffffff" stroke-width="1.5"/>
    </svg>
  </section>

  <section class="piece cover" aria-label="Brand cover panel">
    <div class="brand">
      <div class="wordmark on-colour">TALVORA MED</div>
      <div class="tagline light">Health Care Diagnostic</div>
    </div>
    <div class="cross-band vertical" role="img" aria-label="Column of white and pale teal medical crosses"></div>
  </section>

  <section class="piece letterhead" aria-label="Letterhead">
    <div class="brand">
      <div class="wordmark">TALVORA MED</div>
      <div class="tagline">Health Care Diagnostic</div>
    </div>
    <div class="lines"><span></span><span></span><span></span><span></span><span></span><span></span><span></span><span></span></div>
    <div class="cross-band" role="img" aria-label="Scattered medical cross pattern in teal and blue"></div>
  </section>

  <section class="piece envelope" aria-label="Envelope">
    <svg class="flap" width="330" height="70" viewBox="0 0 330 70" aria-hidden="true">
      <polygon points="0,0 330,0 165,70" fill="#3b5fb0"/>
    </svg>
    <div class="brand">
      <div class="wordmark">TALVORA MED</div>
      <div class="tagline">Health Care Diagnostic</div>
    </div>
    <div class="cross-band" role="img" aria-label="Scattered medical cross pattern in teal and blue"></div>
  </section>

  <section class="piece folder" aria-label="Presentation folder">
    <div class="brand">
      <div class="wordmark on-colour">TALVORA MED</div>
      <div class="tagline light">Health Care Diagnostic</div>
    </div>
    <div class="cross-band blue" role="img" aria-label="Scattered white medical cross pattern"></div>
  </section>

  <section class="piece slip" aria-label="Compliments slip">
    <div class="accent"></div>
    <div class="brand">
      <div class="wordmark">TALVORA MED</div>
      <div class="tagline">Health Care Diagnostic</div>
    </div>
    <div class="cross-band" role="img" aria-label="Scattered medical cross pattern in teal and blue"></div>
  </section>

  <section class="piece badge" aria-label="Staff ID badge">
    <div class="photo" role="img" aria-label="Staff portrait photo"></div>
    <div class="name">Dr. Elias Moran</div>
    <div class="role">Chief Radiologist</div>
    <div class="cross-band blue" role="img" aria-label="Scattered white medical cross pattern"></div>
  </section>

  <section class="piece mini-white" aria-label="Appointment card">
    <div class="brand">
      <div class="wordmark">TALVORA MED</div>
      <div class="tagline">Health Care Diagnostic</div>
    </div>
    <div class="cross-band" role="img" aria-label="Scattered medical cross pattern in teal and blue"></div>
  </section>

  <section class="piece mini-blue" aria-label="Appointment card, reverse">
    <div class="wordmark on-colour">TALVORA MED</div>
  </section>

  <section class="piece tote" aria-label="Tote bag print">
    <div class="strap"></div>
    <div class="edge"></div>
    <div class="brand">
      <div class="wordmark">TALVORA MED</div>
      <div class="tagline">Health Care Diagnostic</div>
    </div>
    <div class="cross-band" role="img" aria-label="Scattered medical cross pattern in teal and blue"></div>
  </section>

</body>
</html>
```